Very clean, very simple business card needed.

I am looking for a VERY simple business card. I have attached our logo. I would like it to be a mainly white card. I have picked double sided but would be open to single as well. I want the overall feel to be simple, classic, and professional. Thank you.

Industry/Entity Type

Consultant

Contact Information for Business Card

Daniel Fenwick

2870 North 9th Avenue, Summit Floor, Larkfield, Northland 60871
dan@belmorevista.com
www.belmorevista.com

Font styles to use
Serif

Colors

Designer to choose colors to be used in the design.

Requirements
Must have
• The business card details and in an editable form to change the names and emails of employees easily.
Nice to have
• n/a
Should not have
• Pictures, big lines and stripes, too much color.

```html
<!DOCTYPE html>
<html lang="en">
<head>
<meta charset="utf-8">
<title>Belmore Vista – Business Card</title>
<link rel="stylesheet" href="https://fonts.googleapis.com/css2?family=Libre+Baskerville:wght@400&display=swap">
<style>
  :root {
    --navy: #2f2b7e;
    --navy-deep: #25216a;
    --paper: #ffffff;
    --backdrop: #e9e9ec;
    --ink: #2f2b7e;
    --serif: "Libre Baskerville", Georgia, serif;
  }
  * { box-sizing: border-box; margin: 0; padding: 0; }
  html, body {
    width: 1200px;
    height: 660px;
    overflow: hidden;
    background: var(--backdrop);
    font-family: var(--serif);
  }
  .sheet {
    position: relative;
    width: 1200px;
    height: 660px;
    display: flex;
    align-items: center;
    justify-content: center;
    gap: 50px;
  }
  .card {
    position: relative;
    width: 525px;
    height: 300px;
    box-shadow: 0 6px 18px rgba(0,0,0,0.18);
    overflow: hidden;
  }

  /* Front */
  .card--front {
    background: linear-gradient(135deg, var(--navy) 0%, var(--navy-deep) 100%);
    display: flex;
    align-items: center;
    justify-content: center;
  }
  .brand {
    display: flex;
    align-items: center;
    gap: 12px;
    font-family: var(--serif);
    font-weight: 400;
    letter-spacing: 0.12em;
    text-transform: uppercase;
    white-space: nowrap;
  }
  .brand__square { width: 16px; height: 16px; flex: 0 0 16px; }
  .card--front .brand { color: var(--paper); font-size: 22px; }
  .card--front .brand__square { background: var(--paper); }

  /* Back */
  .card--back { background: var(--paper); }
  .edge {
    position: absolute;
    left: 0; right: 0;
    height: 14px;
  }
  .edge--top { top: 0; }
  .edge--bottom { bottom: 0; }
  .edge__band {
    position: absolute;
    left: 0; right: 0;
    height: 7px;
    background: var(--navy);
  }
  .edge__rule {
    position: absolute;
    left: 0; right: 0;
    height: 2px;
    background: var(--navy);
  }
  .edge--top .edge__band { top: 0; }
  .edge--top .edge__rule { top: 10px; }
  .edge--bottom .edge__band { bottom: 0; }
  .edge--bottom .edge__rule { bottom: 10px; }

  .card--back .brand {
    position: absolute;
    top: 62px;
    left: 0; right: 0;
    justify-content: center;
    color: var(--ink);
    font-size: 20px;
  }
  .card--back .brand__square { background: var(--navy); }

  .details {
    position: absolute;
    top: 140px;
    left: 40px;
    right: 30px;
    display: flex;
    align-items: stretch;
    color: var(--ink);
  }
  .person {
    flex: 0 0 220px;
    padding-top: 50px;
    padding-right: 22px;
    text-align: right;
  }
  .person__name {
    font-size: 14px;
    letter-spacing: 0.08em;
    text-transform: uppercase;
    white-space: nowrap;
  }
  .person__title {
    margin-top: 6px;
    font-size: 11.5px;
    letter-spacing: 0.06em;
    white-space: nowrap;
  }
  .divider {
    width: 1.5px;
    flex: 0 0 1.5px;
    background: var(--navy);
  }
  .contact {
    padding-left: 16px;
    font-size: 11.5px;
    line-height: 1.65;
    list-style: none;
    white-space: nowrap;
  }
</style>
</head>
<body>
  <main class="sheet">
    <section class="card card--front" aria-label="Card front">
      <div class="brand">
        <span class="brand__square"></span>
        <span class="brand__name">Belmore Vista</span>
      </div>
    </section>

    <section class="card card--back" aria-label="Card back">
      <div class="edge edge--top"><span class="edge__band"></span><span class="edge__rule"></span></div>

      <div class="brand">
        <span class="brand__square"></span>
        <span class="brand__name">Belmore Vista</span>
      </div>

      <div class="details">
        <div class="person">
          <p class="person__name">Daniel Fenwick</p>
          <p class="person__title">Founder and Principal</p>
        </div>
        <div class="divider"></div>
        <ul class="contact">
          <li class="contact__email">dan@belmorevista.com</li>
          <li class="contact__web">www.belmorevista.com</li>
          <li class="contact__street">2870 North 9th Avenue</li>
          <li class="contact__floor">Summit Floor</li>
          <li class="contact__city">Larkfield, Northland 60871</li>
        </ul>
      </div>

      <div class="edge edge--bottom"><span class="edge__rule"></span><span class="edge__band"></span></div>
    </section>
  </main>
</body>
</html>
```